Business Card Design Project

I have a need for a business card designed. I have a logo.. but need looking for a nice card to go with it. The school is called The Bramblewood Fighting Hall is the name of the school. Some ideas for what I want on the card.
Guru Rick Fennaway
over 25 years martial arts experience
Private and group lessons
kids and adult classes
No contracts or testing fees
styles we teach are escrima, silat, kenpo, and MMA
website is www.bramblewoodhall.net
phone is 555-204-7318
visit us on face book at https://www.fakebooksite.com/pages/The-Bramblewood-Fighting-Hall/482096315720448

Target Market(s)

adults 1st kids second.

Industry/Entity Type

School

Requirements
Must have
• Guru Rick Fennaway
Private and group lessons
phone is 555-204-7318

```html
<!DOCTYPE html>
<html lang="en">
<head>
<meta charset="utf-8">
<title>The Bramblewood Fighting Hall – Business Card</title>
<link href="https://fonts.googleapis.com/css2?family=Open+Sans:ital,wght@0,400;0,700;0,800;1,600&display=swap" rel="stylesheet">
<style>
  :root {
    --stage: #eef8fa;
    --card-edge: #0b0b0b;
    --red-deep: #7a0e06;
    --red-mid: #a81508;
    --glow: #e2621c;
    --gold-line: #f3d21b;
    --yellow: #f6ec12;
    --ink: #111111;
    --white: #ffffff;
    --navy: #13307f;
    --panel-black: #121212;
    --body-font: "Open Sans", Arial, sans-serif;
  }
  * { box-sizing: border-box; margin: 0; padding: 0; }
  html, body { width: 1200px; height: 788px; overflow: hidden; }
  body { background: var(--stage); font-family: var(--body-font); position: relative; }

  .card { position: absolute; background: var(--card-edge); }

  /* Front */
  .card-front { left: 32px; top: 330px; width: 708px; height: 405px; padding: 13px; }
  .card-front .face {
    width: 100%; height: 100%;
    border: 2px solid var(--gold-line);
    background: linear-gradient(180deg, var(--red-mid) 0%, var(--red-deep) 100%);
    display: flex; align-items: center; justify-content: center;
  }

  .school-name {
    display: flex; align-items: center; gap: 14px;
    color: var(--yellow); font-weight: 800; text-transform: uppercase;
    text-align: center; line-height: 1.05;
  }
  .school-name .mark { width: 22px; height: 22px; background: var(--yellow); border-radius: 50%; flex: none; }
  .card-front .school-name { font-size: 34px; max-width: 360px; }

  /* Back */
  .card-back { left: 770px; top: 30px; width: 402px; height: 702px; padding: 17px 15px; }
  .card-back .face {
    width: 100%; height: 100%;
    display: flex; flex-direction: column;
    background: radial-gradient(ellipse 70% 42% at 50% 28%, var(--glow) 0%, var(--red-mid) 55%, var(--red-deep) 100%);
  }
  .back-brand { height: 322px; display: flex; align-items: center; justify-content: center; }
  .back-brand .school-name { font-size: 30px; max-width: 300px; }

  .styles {
    color: var(--white); font-weight: 800; text-align: center;
    font-size: 35px; line-height: 1.12; letter-spacing: -0.3px;
    padding-top: 12px; height: 110px;
    text-shadow: 2px 2px 2px rgba(0,0,0,.55);
  }
  .styles .small { font-size: 26px; }

  .instructor { background: var(--yellow); color: var(--ink); text-align: center; padding: 8px 0 7px; }
  .instructor .name { font-weight: 700; font-size: 24px; line-height: 1.2; }
  .instructor .exp { font-style: italic; font-weight: 600; font-size: 15.5px; }

  .offers {
    background: var(--panel-black); color: var(--white);
    margin: 4px 0 4px; border: 1px solid #ddd;
    padding: 8px 0 8px 36px; font-size: 20px; line-height: 1.45;
    list-style: none;
  }
  .offers li::before { content: "•"; margin-right: 8px; }

  .contact { background: var(--navy); color: var(--white); text-align: center; flex: 1; padding-top: 6px; }
  .contact .phone { font-weight: 700; font-size: 31px; line-height: 1.15; letter-spacing: 1px; }
  .contact .web { font-weight: 700; font-size: 17px; letter-spacing: 1.5px; }
</style>
</head>
<body>
  <section class="card card-front" aria-label="Business card front">
    <div class="face">
      <div class="school-name"><span class="mark"></span><span>The Bramblewood Fighting Hall</span></div>
    </div>
  </section>

  <section class="card card-back" aria-label="Business card back">
    <div class="face">
      <div class="back-brand">
        <div class="school-name"><span class="mark"></span><span>The Bramblewood Fighting Hall</span></div>
      </div>
      <h2 class="styles">ESKRIMA, SILAT,<br>KENPO <span class="small">AND</span> MMA</h2>
      <div class="instructor">
        <div class="name">Guru Rick Fennaway</div>
        <div class="exp">over 25 years martial arts experience</div>
      </div>
      <ul class="offers">
        <li>Private and Group Lessons</li>
        <li>No Contracts or Testing Fees</li>
      </ul>
      <div class="contact">
        <div class="phone">555-204-7318</div>
        <div class="web">www.bramblewoodhall.net</div>
      </div>
    </div>
  </section>
</body>
</html>
```